Web Design for Solar Energy Consultancy Company

~ May 3, 2017 Update ~
As our project is rapidly progressing towards its completion, we started building up the list of designs that attracted the most of the team's attention. Additional submittals are still most welcome. Before submitting your proposal, however, we can recommend to review the concepts that received 4 stars as these are the ones that, in our opinion, most closely match the brief's requirements. Thank you!!
~ April 30, 2017 Update ~
The project deadline has been extended to attract a broader design community and to better tailor the final design to the requirements of the project.
A "light", "clean" (minimalistic), professionally looking, unique design is expected. Please, try to avoid industry cliches. Also, please use green, which became another industry cliche, with great caution. The brief provides minimum details to foster creativity. With the same notion in mind, the page content information is not provided.
Thank you for your feedback and support of the project!!
~ April 22, 2017 Update ~
Additional comments after starting receiving more designs:
- your attention to the brief's requirements will be highly appreciated. It is expected that the design is unique - standard, commonly used, images, formats and approaches do not fall under this category. There is no need to "bombard" with slightly different variations of the same design. It is expected that a conceptual (preliminary) design is submitted first, and, after it is reviewed (each design will receive a star rating and, if the star rating is greater than 3, a detailed feedback), the requested changes are implemented. We believe this will allow to approach the design process more efficiently and safe additional time to both the Designers's Community and our company. Thank you for understanding.
Clarification, please submit two variations of a design:
1) 1 page "business card" design that the company will be able to use during its startup stage;
2) the fully functional design (as per the requirements outlined below) for the company to transition to after the start-up period is over. Same design principles as developed for option 1 should be used for this variation.
Additional clarification, please note that the news block will not require images (at least during the start-up stage). It is envisioned to be a news feeder.
~ April 21, 2017 Update ~
Preliminary comments after receiving first designs:
- please try to create a unique design, using common elements wisely. Though such solar energy "attributes" as a solar panel or a bulb are very well recognized and allow quickly identify the nature of the business, they also became so common that in many cases a design may seem very similar to the one of others (Oh!, I've already seen this... effect).
- please try to introduce the company's logo unobtrusively. The size and position of the logo should clearly identify the company, but the message should be subtle, the logo should not distract from the main design. Brask's swoosh did not need to occupy have the screen.
- please use the green color with caution as it was with the company's logo. True, it is a green energy. But there is no need for the color to "scream" about it. Use the amount of green and its tone (avoid acid green) wisely.
--------------------------------------------------------------------------------
1. Main Goal
Develop a website that can represent the company to the industry stakeholders and become its "business card" during the start-up stage.
2. Secondary Goal
Develop a structure of a fully functional website that the "business card" design can eventually be transformed to staying consistent with the original design principles.
3. Key Audience
Varolu Corp. is providing consulting and technical services in the area of Solar Energy. The industry stakeholders include project developers, financial community, governmental bodies, OEMs, and competition.
4. Site Map
- HOME
• About
• Services
• Solar Energy
• News
• Contacts
• Social Media
- SERVICES*
- PROJECTS*
- FINANCE*
- TRAINING*
- SOLAR (ENERGY)*
* Maybe inactive / partially functional during the start-up stage.
5. Technical Specifications
Online brochure website during the start-up stage with a capability to be eventually transformed to a fully functional website while preserving the original design principles.
The design to be appealing, "light", professional, and with an intuitive and easy to navigate interface. Modern coding principles supporting efficiency and security to be utilized. Newest industry trends in website coding will be welcome.
The website to be designed so that it would fit well a computer, tablet, or mobile phone screen of any size. Cross-platform functionality to be taken into consideration to ensure that the website is fully functional on any platform.
Company's logo has already been designed and will be shared with the short-listed designers during the final design stage.
6. Interaction
The website will provide information about the company, our services, and projects. In addition, the industry insight, accumulated knowledge, and most recent trends are planned to be shared with stakeholders and attract and retain the audience.
Interaction with designers during the website development is envisioned to go through the following steps:
a) conceptual design - to be proposed by a designer originally. All conceptual designs will be reviewed and a feedback provided to pre-selected designers;
b) (preliminary and) final design - depending on the level of additional changes required can be broken into two steps. After discussing preliminary designs, company images will be provided to the selected finalists, who will compete with their final proposals.
7. Industry Stakeholders
- https://www.quellbrin.com/power/solar-power.- http://www.pakortavon.com/
- http://www.vellitrazo.com/about/company/
- https://www.oruxem.com/energy/index.html
8. Budget
Defined by the project.
9. Timescale
Defined by the project.
12. Additional Info
- No copy-cats, standard graphics, or cliches please!
- Additional information / clarifications will be gladly provided upon request.
- This specification may be updated throughout the project to reflect discussions with / changes proposed by the Designers community.

```html
<!DOCTYPE html>
<html lang="en">
<head>
<meta charset="utf-8">
<title>Varolu Corp — Integrated Consulting &amp; Technical Services</title>
<link href="https://fonts.googleapis.com/css2?family=Montserrat:wght@400;500;600;700&display=swap" rel="stylesheet">
<style>
:root{
  --green:#5aae3c;
  --green-bar:#7dbf42;
  --yellow:#fdbd14;
  --ink:#1f1f1f;
  --text:#444;
  --muted:#8a8a8a;
  --light-bg:#f4f6f2;
  --dark-panel:#262626;
  --footer-bg:#eeeeec;
  --white:#fff;
}
*{box-sizing:border-box;margin:0;padding:0}
html,body{width:1200px;height:2553px;overflow:hidden}
body{font-family:"Montserrat",Arial,sans-serif;color:var(--text);background:var(--white)}
.page{position:relative;width:1200px;height:2553px;overflow:hidden}
.abs{position:absolute}
a{text-decoration:none;color:inherit}

/* header */
.site-header{position:absolute;left:0;top:0;width:1200px;height:89px;background:var(--white)}
.brand{position:absolute;left:65px;top:22px;display:flex;align-items:center;gap:12px}
.brand-dot{width:44px;height:44px;border-radius:50%;background:var(--yellow)}
.brand-name{font-size:22px;font-weight:600;color:#3a3a3a;letter-spacing:1px}
.main-nav a{position:absolute;top:36px;font-size:15px;font-weight:500;color:#333}
.main-nav a.active{color:var(--green)}
.main-nav a.active::after{content:"";position:absolute;left:0;right:0;top:50px;height:3px;background:var(--green)}
.search-btn{position:absolute;left:1071px;top:0;width:61px;height:89px;background:var(--yellow);display:flex;align-items:center;justify-content:center}

/* hero */
.hero{position:absolute;left:0;top:89px;width:1200px;height:583px}
.hero-photo{position:absolute;inset:0;background:linear-gradient(100deg,#7d7f84 0%,#b9bcbf 30%,#9a9ea4 55%,#6f7276 80%,#8c8f94 100%)}
.hero-shade{position:absolute;inset:0;background:rgba(40,40,45,.25)}
.hero-title{position:absolute;left:0;width:1200px;top:150px;text-align:center;color:var(--white);font-size:54px;font-weight:700;line-height:59px;text-transform:uppercase;letter-spacing:.5px}
.hero-sub{position:absolute;left:0;width:1200px;top:286px;text-align:center;color:var(--white);font-size:21px;font-weight:500;line-height:31px}
.hero-sub em{font-style:normal;color:#8fd14a}
.btn-contact{position:absolute;left:497px;top:367px;width:189px;height:50px;background:var(--yellow);color:var(--white);font-size:16px;font-weight:500;display:flex;align-items:center;justify-content:center;border-radius:2px}

/* intro */
.intro{position:absolute;left:0;top:672px;width:1200px;height:269px;background:var(--light-bg)}
.intro-heading{position:absolute;left:80px;top:62px;font-size:24px;font-weight:500;color:var(--ink)}
.intro-tagline{position:absolute;left:80px;top:104px;width:360px;font-size:22px;line-height:31px;color:var(--muted)}
.intro-text{position:absolute;left:519px;top:60px;width:575px;font-size:14.5px;line-height:27px;color:var(--muted)}
.read-more{display:inline-flex;align-items:center;gap:8px;font-size:15px;font-weight:500;color:var(--green)}
.intro .read-more{position:absolute;left:519px;top:184px}

/* services */
.section-title{position:absolute;left:0;width:1200px;text-align:center;font-size:26px;font-weight:600;color:var(--ink)}
.service{position:absolute;width:290px}
.service-icon{position:absolute;left:0;top:0;width:38px;height:38px}
.service-name{position:absolute;left:51px;top:0;font-size:17px;font-weight:500;color:#222;line-height:25px}
.service-desc{position:absolute;left:51px;top:60px;width:240px;font-size:14.5px;line-height:22px;color:var(--muted)}

/* solar split */
.solar{position:absolute;left:0;top:1469px;width:1200px;height:383px}
.solar-photo{position:absolute;left:0;top:0;width:580px;height:383px;background:linear-gradient(180deg,#7fa6c9 0%,#e8c7b0 30%,#3a5b86 38%,#2c4f86 65%,#3f6aa8 100%)}
.solar-panel{position:absolute;left:580px;top:0;width:620px;height:383px;background:var(--dark-panel)}
.solar-heading{position:absolute;left:48px;top:57px;font-size:26px;color:var(--white);font-weight:400}
.solar-text{position:absolute;left:48px;top:114px;width:470px;font-size:14.5px;line-height:27px;color:#e2e2e2}
.solar-panel .read-more{position:absolute;left:48px;top:314px}

/* news */
.news-item{position:absolute;top:1993px;width:340px;height:112px}
.news-photo{position:absolute;left:0;top:0;width:114px;height:112px}
.news-date{position:absolute;left:146px;top:10px;font-size:15px;color:#555}
.news-title{position:absolute;left:146px;top:37px;width:190px;font-size:15px;font-weight:500;line-height:22px;color:#222}
.news-item .read-more{position:absolute;left:146px;top:94px}

/* footer */
.site-footer{position:absolute;left:0;top:2158px;width:1200px;height:382px;background:var(--footer-bg)}
.footer-bar{position:absolute;left:0;top:2540px;width:1200px;height:13px;background:var(--green-bar)}
.site-footer .brand{left:65px;top:56px}
.footer-about{position:absolute;left:65px;top:150px;width:250px;font-size:14.5px;line-height:23px;color:#444}
.footer-about em{font-style:normal;color:var(--green)}
.footer-heading{position:absolute;top:90px;font-size:16px;font-weight:600;color:var(--ink)}
.quick-links{position:absolute;left:384px;top:136px;list-style:none}
.quick-links li{font-size:14.5px;line-height:27px;color:#444}
.contact-list{position:absolute;left:574px;top:136px;list-style:none}
.contact-list li{display:flex;align-items:center;gap:14px;font-size:14.5px;color:#444;height:38px}
.contact-list li.phone{font-weight:600;color:#222}
.newsletter-label{position:absolute;left:880px;top:138px;font-size:14.5px;color:#444}
.newsletter-form{position:absolute;left:880px;top:174px;display:flex}
.newsletter-input{width:211px;height:28px;background:var(--green-bar);color:var(--white);font-size:14px;padding-left:20px;display:flex;align-items:center}
.newsletter-ok{width:41px;height:28px;background:var(--yellow);color:var(--white);font-size:14px;font-weight:700;display:flex;align-items:center;justify-content:center}
</style>
</head>
<body>
<div class="page">

  <header class="site-header">
    <a class="brand" href="#"><span class="brand-dot"></span><span class="brand-name">VAROLU CORP</span></a>
    <nav class="main-nav">
      <a class="active" href="#" style="left:309px">Home</a>
      <a href="#" style="left:412px">Services</a>
      <a href="#" style="left:534px">Project</a>
      <a href="#" style="left:645px">Finance</a>
      <a href="#" style="left:760px">Training</a>
      <a href="#" style="left:878px">Solar Energy</a>
    </nav>
    <a class="search-btn" href="#" aria-label="Search">
      <svg width="20" height="20" viewBox="0 0 20 20"><circle cx="8" cy="8" r="6" fill="none" stroke="#fff" stroke-width="2.6"/><line x1="12.5" y1="12.5" x2="18" y2="18" stroke="#fff" stroke-width="3" stroke-linecap="round"/></svg>
    </a>
  </header>

  <section class="hero">
    <div class="hero-photo" role="img" aria-label="Business team of four consultants meeting around a table with a laptop"></div>
    <div class="hero-shade"></div>
    <h1 class="hero-title">Integrated Consulting &amp;<br>Technical Services</h1>
    <p class="hero-sub">We providing consulting and technical services in<br>the area of <em>Solar Energy</em></p>
    <a class="btn-contact" href="#">Contact Us</a>
  </section>

  <section class="intro">
    <h2 class="intro-heading">INTRODUCING VAROLU CORP</h2>
    <p class="intro-tagline">Varolu Corp Solar is a complete turnkey solution provider in the Solar Energy sector.</p>
    <p class="intro-text">Sed ut perspiciatis unde omnis iste natus error sit voluptatem accusantium doloremque laudantium, totam rem aperiam, eaque ipsa quae ab illo inventore veritatis et quasi architecto beatae vitae dicta sunt explicabo. Nemo enim ipsam voluptatem quia voluptas sit</p>
    <a class="read-more" href="#">Read More <svg width="11" height="11" viewBox="0 0 11 11"><path d="M1 5.5h7M5 2l3.5 3.5L5 9" fill="none" stroke="currentColor" stroke-width="2"/></svg></a>
  </section>

  <h2 class="section-title" style="top:996px">FEATURED SERVICES</h2>

  <div class="service" style="left:82px;top:1072px">
    <svg class="service-icon" viewBox="0 0 38 38" fill="var(--yellow)"><circle cx="12" cy="8" r="5"/><rect x="5" y="15" width="14" height="18" rx="3"/><circle cx="26" cy="11" r="4"/><rect x="20" y="17" width="12" height="16" rx="3"/></svg>
    <h3 class="service-name">Bussiness Services<br>Consulting</h3>
    <p class="service-desc">Lorem ipsum dolor sit amet, consectetur adipiscing elit, sed do eiusmod tempo</p>
  </div>
  <div class="service" style="left:465px;top:1072px">
    <svg class="service-icon" viewBox="0 0 38 38" fill="var(--yellow)"><circle cx="16" cy="10" r="7"/><path d="M3 34c0-9 6-14 13-14s13 5 13 14z"/><circle cx="30" cy="28" r="7" stroke="#fff" stroke-width="2"/></svg>
    <h3 class="service-name">Financing Services<br>Management</h3>
    <p class="service-desc">Lorem ipsum dolor sit amet, consectetur adipiscing elit, sed do eiusmod tempo</p>
  </div>
  <div class="service" style="left:837px;top:1072px">
    <svg class="service-icon" viewBox="0 0 38 38" fill="var(--yellow)"><circle cx="15" cy="13" r="7"/><path d="M2 35c0-9 6-14 13-14s13 5 13 14z"/><circle cx="30" cy="8" r="7"/></svg>
    <h3 class="service-name">Customer Services<br>Team</h3>
    <p class="service-desc">Lorem ipsum dolor sit amet, consectetur adipiscing elit, sed do eiusmod tempo</p>
  </div>
  <div class="service" style="left:82px;top:1277px">
    <svg class="service-icon" viewBox="0 0 38 38" fill="none" stroke="var(--yellow)" stroke-width="3"><rect x="3" y="5" width="32" height="22" rx="2"/><path d="M3 16h32M14 5v22M24 5v22M19 27v8M12 35h14"/></svg>
    <h3 class="service-name">Solar Pump<br>Services</h3>
    <p class="service-desc">Lorem ipsum dolor sit amet, consectetur adipiscing elit, sed do eiusmod tempo</p>
  </div>
  <div class="service" style="left:462px;top:1277px">
    <svg class="service-icon" viewBox="0 0 38 38" fill="var(--yellow)"><path d="M19 4l4 10 10-2-6 9 7 6-10 1-5 9-5-9-10-1 7-6-6-9 10 2z"/></svg>
    <h3 class="service-name">Solar Pump<br>Services</h3>
    <p class="service-desc">Lorem ipsum dolor sit amet, consectetur adipiscing elit, sed do eiusmod tempo</p>
  </div>
  <div class="service" style="left:837px;top:1277px">
    <svg class="service-icon" viewBox="0 0 38 38" fill="var(--yellow)"><circle cx="19" cy="19" r="9"/><g stroke="var(--yellow)" stroke-width="3"><path d="M19 1v6M19 31v6M1 19h6M31 19h6M6 6l4 4M28 28l4 4M6 32l4-4M28 10l4-4"/></g></svg>
    <h3 class="service-name">EPC<br>Services</h3>
    <p class="service-desc">Lorem ipsum dolor sit amet, consectetur adipiscing elit, sed do eiusmod tempo</p>
  </div>

  <section class="solar">
    <div class="solar-photo" role="img" aria-label="Field of blue solar panels under a pastel sunset sky"></div>
    <div class="solar-panel">
      <h2 class="solar-heading">SOLAR ENERGY</h2>
      <p class="solar-text">Solar energy can be captured in a variety of ways. There are two key methods to harness this resource to produce electricitySed ut perspiciatis unde omnis iste natus error sit voluptatem. accusantium doloremque laudantium, totam rem aperiam eaque ipsa quae ab illo inventore veritatis et quasi architecto beatae vitae dicta sunt explicabo. Nemo enim ipsam</p>
      <a class="read-more" href="#">Read More <svg width="11" height="11" viewBox="0 0 11 11"><path d="M1 5.5h7M5 2l3.5 3.5L5 9" fill="none" stroke="currentColor" stroke-width="2"/></svg></a>
    </div>
  </section>

  <h2 class="section-title" style="top:1910px">LATEST NEWS</h2>

  <article class="news-item" style="left:65px">
    <div class="news-photo" role="img" aria-label="Portrait of a smiling businesswoman" style="background:linear-gradient(160deg,#f3f3f3,#d9c6a4 60%,#2c2c30)"></div>
    <span class="news-date">APR 22</span>
    <h3 class="news-title">Sed quia consequuntur magni dolores eos.</h3>
    <a class="read-more" href="#">Read More <svg width="11" height="11" viewBox="0 0 11 11"><path d="M1 5.5h7M5 2l3.5 3.5L5 9" fill="none" stroke="currentColor" stroke-width="2"/></svg></a>
  </article>
  <article class="news-item" style="left:420px">
    <div class="news-photo" role="img" aria-label="Portrait of a businessman in a dark suit" style="background:linear-gradient(160deg,#f1f1f1,#c9ab93 55%,#2a2d35)"></div>
    <span class="news-date">APR 22</span>
    <h3 class="news-title">Sed quia consequuntur magni dolores eos.</h3>
    <a class="read-more" href="#">Read More <svg width="11" height="11" viewBox="0 0 11 11"><path d="M1 5.5h7M5 2l3.5 3.5L5 9" fill="none" stroke="currentColor" stroke-width="2"/></svg></a>
  </article>
  <article class="news-item" style="left:776px">
    <div class="news-photo" role="img" aria-label="Portrait of a smiling man in front of a blue backdrop" style="background:linear-gradient(160deg,#3d5f86,#b69480 55%,#25344a)"></div>
    <span class="news-date">APR 22</span>
    <h3 class="news-title">Sed quia consequuntur magni dolores eos.</h3>
    <a class="read-more" href="#">Read More <svg width="11" height="11" viewBox="0 0 11 11"><path d="M1 5.5h7M5 2l3.5 3.5L5 9" fill="none" stroke="currentColor" stroke-width="2"/></svg></a>
  </article>

  <footer class="site-footer">
    <a class="brand" href="#"><span class="brand-dot"></span><span class="brand-name">VAROLU CORP</span></a>
    <p class="footer-about"><em>Solar energy</em> was started by executive passed out from Kestor Institute and with their experience in the best power companies across the world; they are committed to deliver only the best</p>

    <h4 class="footer-heading" style="left:381px">QUICK LINKS</h4>
    <ul class="quick-links">
      <li>Service</li><li>Finance</li><li>Training</li><li>Project</li><li>Solar Energy</li>
    </ul>

    <h4 class="footer-heading" style="left:574px">CONTACT US</h4>
    <ul class="contact-list">
      <li><svg width="11" height="15" viewBox="0 0 11 15"><path d="M5.5 0a5.5 5.5 0 0 0-5.5 5.5C0 9.5 5.5 15 5.5 15S11 9.5 11 5.5A5.5 5.5 0 0 0 5.5 0z" fill="var(--yellow)"/><circle cx="5.5" cy="5.5" r="2" fill="#fff"/></svg>48 ARDEL AVE, MARLOW NJ 0731</li>
      <li class="phone"><svg width="12" height="13" viewBox="0 0 12 13"><path d="M3 0l2 3-1.5 1.5c.8 2 2 3.2 4 4L9 7l3 2-1.5 3C5 11.5.5 7 0 1.5z" fill="var(--yellow)"/></svg>(0100) 7342-6618</li>
      <li><svg width="12" height="9" viewBox="0 0 12 9"><rect width="12" height="9" fill="var(--yellow)"/><path d="M0 0l6 5 6-5" fill="none" stroke="#fff" stroke-width="1.3"/></svg>info@varolucorp.com</li>
    </ul>

    <h4 class="footer-heading" style="left:880px">NEWS LETTER</h4>
    <p class="newsletter-label">Sign up Our Newsletter :</p>
    <form class="newsletter-form">
      <span class="newsletter-input">Email</span>
      <span class="newsletter-ok">OK</span>
    </form>
  </footer>
  <div class="footer-bar"></div>

</div>
</body>
</html>
```